Real Estate Company / Capital Needs Cards!

need business cards designed using the logos that were just designed by brightquill.

Target Market(s)

Investors and clients looking to purchase real estate or invest in the business.

Industry/Entity Type

Business

Requirements
Must have
• two designs - one for the real estate logo and one for the capital logo, similar but slightly different.
Nice to have
• something to make it pop (perhaps on the back)
Should not have
• much color

```html
<!DOCTYPE html>
<html lang="en">
<head>
<meta charset="utf-8">
<title>Norvale Business Cards</title>
<link rel="stylesheet" href="https://fonts.googleapis.com/css2?family=Cinzel:wght@400;600&display=swap">
<style>
:root{
  --backdrop:#1a1a1b;
  --card-dark:#232325;
  --card-white:#f7f7f7;
  --silver-light:#e9e9ea;
  --silver-mid:#c4c4c6;
  --silver-dark:#9a9a9c;
  --ink-dark:#3a3a3c;
  --ink-light:#d6d6d8;
  --rule:#b8b8ba;
}
*{box-sizing:border-box;margin:0;padding:0}
html,body{width:1200px;height:1000px;overflow:hidden;background:var(--backdrop)}
body{position:relative;font-family:"Cinzel",serif;}
.card{position:absolute;border-radius:10px;overflow:hidden}
.card--white{background:var(--card-white)}
.card--dark{background:var(--card-dark);color:var(--ink-light)}

.capital-front{left:150px;top:40px;width:280px;height:440px}
.capital-back{left:700px;top:40px;width:280px;height:440px}
.estate-front{left:80px;top:560px;width:470px;height:290px}
.estate-back{left:640px;top:560px;width:470px;height:290px}

.dark-panel{position:absolute;background:var(--card-dark)}
.capital-front .dark-panel{left:32px;right:14px;top:0;height:340px}
.capital-front .panel-rule{position:absolute;left:32px;right:14px;top:350px;height:1px;background:var(--rule)}
.estate-front .dark-panel{left:0;right:0;top:40px;height:162px}

.brand{position:absolute;display:flex;align-items:center;gap:14px;color:var(--silver-mid)}
.brand-square{width:54px;height:54px;background:var(--silver-mid);border-radius:4px;flex:none}
.brand-text{display:flex;flex-direction:column;align-items:center;line-height:1}
.brand-name{font-size:36px;font-weight:400;letter-spacing:2px}
.brand-sub{font-size:14px;letter-spacing:3px;margin-top:6px}
.capital-front .brand{left:32px;right:14px;top:140px;flex-direction:column;gap:16px}
.estate-front .brand{left:0;right:0;top:78px;justify-content:center}

.web{position:absolute;left:0;right:0;text-align:center;color:var(--ink-dark);white-space:nowrap}
.capital-front .web{left:32px;right:14px;top:366px;font-size:11px;letter-spacing:1.5px}
.estate-front .web{top:230px;font-size:13px;letter-spacing:3px}

.silver-band{position:absolute;left:0;right:0;background:linear-gradient(180deg,var(--silver-light),var(--silver-mid) 55%,var(--silver-dark));color:var(--ink-dark)}
.capital-back .silver-band{top:52px;height:62px;text-align:center;padding-top:12px}
.estate-back .silver-band{top:36px;height:82px;display:flex;align-items:center;justify-content:space-between;padding:0 40px 0 66px}
.person-name{font-size:18px;letter-spacing:1px}
.person-role{font-size:11px;letter-spacing:2px;margin-top:4px}
.direct{font-size:11px;letter-spacing:1px;line-height:1.45}
.capital-back .direct{position:absolute;left:0;right:0;top:130px;text-align:center;color:var(--ink-light)}
.estate-back .direct{color:var(--ink-dark);font-size:11px}

.office{position:absolute;font-size:11.5px;letter-spacing:1px;line-height:1.5;color:var(--ink-light)}
.office-name{font-weight:600;font-size:12px;margin-bottom:8px}
.capital-back .office{left:0;right:0;top:290px;text-align:center}
.estate-back .office{left:92px;top:150px}
</style>
</head>
<body>

<section class="card card--white capital-front">
  <div class="dark-panel"></div>
  <div class="brand">
    <span class="brand-square"></span>
    <div class="brand-text">
      <span class="brand-name">NORVALE</span>
      <span class="brand-sub">CAPITAL, LLC</span>
    </div>
  </div>
  <div class="panel-rule"></div>
  <p class="web">WWW.NORVALECAPITAL.COM</p>
</section>

<section class="card card--dark capital-back">
  <div class="silver-band">
    <p class="person-name">Owen R. Hartley</p>
    <p class="person-role">Managing Partner</p>
  </div>
  <p class="direct">owen@norvalecapital.com<br>555 214 7730</p>
  <div class="office">
    <p class="office-name">NORVALE CAPITAL, LLC</p>
    <p>118 Elm Park Avenue,<br>Suite B, Fairhaven, OH 45201<br>Tel: - 555 310 6624<br>Fax: - 555 310 6625</p>
  </div>
</section>

<section class="card card--white estate-front">
  <div class="dark-panel"></div>
  <div class="brand">
    <span class="brand-square"></span>
    <div class="brand-text">
      <span class="brand-name">NORVALE</span>
      <span class="brand-sub">REAL ESTATE</span>
    </div>
  </div>
  <p class="web">WWW.NORVALEREALESTATE.COM</p>
</section>

<section class="card card--dark estate-back">
  <div class="silver-band">
    <p class="person-name">Owen Hartley</p>
    <p class="direct">owen@norvalerealestate.com<br>555 214 7730</p>
  </div>
  <div class="office">
    <p class="office-name">NORVALE REAL ESTATE</p>
    <p>118 Elm Park Avenue, Suite B, Fairhaven, OH 45201<br>Tel: - 555 310 6624<br>Fax: - 555 310 6625</p>
  </div>
</section>

</body>
</html>
```